Election Results Powerpoint

Hello!
I'm in need of a way to display election results for multiple students' union elections. My thinking is a Powerpoint template which can be easily edited/updated, however if you can think of another way that this could be done which doesn't require specialist software I'm open to suggestions.
The display must be able to accommodate demonstrating an 'Alternative Vote' election (http://www.newsharbor.example/news/politics-48213097). Several candidates may stand for one position, and the display must accommodate being able to show a picture of each candidate, transfer of votes from an eliminated candidate to other candidates and be able to show the 'quota' for each round until we have a winner.
The display must be simple to understand for someone who has no prior knowledge of elections & if possible be exciting in its presentation. These results will be displayed to a large crowd and will be the method for people to find out if their candidate has won.
I have attached the logo of the organisation which must be included in the design.
A possible example of what you need to aim for is here - http://www.clipvault.example/watch?v=Qk7RtpLmWzN&t=91m0s - But I'm sure you lovely people out there can do better :)
Thanks

```html
<!DOCTYPE html>
<html lang="en">
<head>
<meta charset="utf-8">
<title>Election Results – Project Title</title>
<link href="https://fonts.googleapis.com/css2?family=Dosis:wght@600;700&family=Open+Sans:wght@700&display=swap" rel="stylesheet">
<style>
  :root {
    --red: #c8232a;
    --red-light: #e0484d;
    --black: #111111;
    --white: #ffffff;
    --paper: #e7e7e7;
    --paper-dark: #dcdcdc;
    --photo-light: #c9a27c;
    --photo-dark: #6b4a33;
  }
  html, body {
    margin: 0;
    padding: 0;
    overflow: hidden;
  }
  .slide {
    position: relative;
    width: 1200px;
    height: 900px;
    overflow: hidden;
    background: radial-gradient(ellipse at 50% 40%, var(--paper) 0%, var(--paper-dark) 100%);
    font-family: "Dosis", sans-serif;
  }
  .slide-title {
    position: absolute;
    left: 18px;
    top: 26px;
    margin: 0;
    color: var(--red);
    font-weight: 700;
    font-size: 54px;
    line-height: 1;
    letter-spacing: 0.5px;
  }
  .title-rule {
    position: absolute;
    left: 18px;
    top: 102px;
    width: 1110px;
    height: 6px;
    background: var(--red);
  }
  .union-mark {
    position: absolute;
    right: 14px;
    top: 14px;
    display: flex;
    align-items: center;
    gap: 10px;
    color: var(--red);
    font-weight: 700;
    font-size: 20px;
    text-transform: uppercase;
  }
  .union-mark .dot {
    width: 56px;
    height: 56px;
    border-radius: 50%;
    background: var(--red);
  }
  .candidate {
    position: absolute;
    width: 580px;
    height: 150px;
  }
  .col-left { left: 18px; }
  .col-right { left: 635px; }
  .row-1 { top: 144px; }
  .row-2 { top: 302px; }
  .row-3 { top: 459px; }
  .row-4 { top: 626px; }
  .candidate-photo {
    position: absolute;
    left: 0;
    top: 0;
    width: 114px;
    height: 138px;
    border: 3px solid var(--white);
    background: linear-gradient(160deg, var(--photo-light) 0%, #b48560 55%, var(--photo-dark) 100%);
    box-shadow: 0 1px 3px rgba(0,0,0,0.25);
  }
  .candidate-banner {
    position: absolute;
    left: 118px;
    top: 8px;
    width: 440px;
    height: 70px;
  }
  .candidate-banner svg {
    position: absolute;
    inset: 0;
    filter: drop-shadow(0 2px 2px rgba(0,0,0,0.25));
  }
  .candidate-name {
    position: absolute;
    left: 20px;
    top: 0;
    height: 70px;
    line-height: 70px;
    color: var(--white);
    font-weight: 600;
    font-size: 28px;
    text-transform: uppercase;
    white-space: nowrap;
  }
  .candidate-votes {
    position: absolute;
    left: 318px;
    top: 0;
    width: 90px;
    height: 70px;
    line-height: 70px;
    text-align: center;
    color: var(--white);
    font-family: "Open Sans", sans-serif;
    font-weight: 700;
    font-size: 29px;
  }
  .vote-bar {
    position: absolute;
    left: 118px;
    top: 96px;
    width: 381px;
    height: 33px;
    box-sizing: border-box;
    background: var(--red);
    border: 1px solid var(--red-light);
    border-radius: 0 8px 8px 0;
    box-shadow: 0 2px 3px rgba(0,0,0,0.2);
    overflow: hidden;
  }
  .vote-bar-fill {
    position: absolute;
    left: 0;
    top: 0;
    width: 166px;
    height: 100%;
    background: linear-gradient(180deg, #555 0%, #1d1d1d 50%, #000 100%);
    clip-path: polygon(0 0, 150px 0, 100% 50%, 150px 100%, 0 100%);
  }
  .footer-band {
    position: absolute;
    left: 0;
    bottom: 0;
    width: 1200px;
    height: 45px;
    background: var(--red);
  }
</style>
</head>
<body>
<main class="slide">
  <h1 class="slide-title">PROJECT TITLE HERE</h1>
  <div class="title-rule"></div>
  <div class="union-mark"><span>Hillcrest SU</span><span class="dot"></span></div>

  <!-- candidate template -->
  <section class="candidate col-left row-1">
    <div class="candidate-photo" role="img" aria-label="Candidate photo"></div>
    <div class="candidate-banner">
      <svg width="440" height="70" viewBox="0 0 440 70"><polygon points="0,0 322,0 284,70 0,70" fill="#c8232a"/><polygon points="330,0 438,0 400,70 292,70" fill="#111"/></svg>
      <span class="candidate-name">Owen Bradley Carter</span>
      <span class="candidate-votes">295</span>
    </div>
    <div class="vote-bar"><div class="vote-bar-fill"></div></div>
  </section>

  <section class="candidate col-left row-2">
    <div class="candidate-photo" role="img" aria-label="Candidate photo"></div>
    <div class="candidate-banner">
      <svg width="440" height="70" viewBox="0 0 440 70"><polygon points="0,0 322,0 284,70 0,70" fill="#c8232a"/><polygon points="330,0 438,0 400,70 292,70" fill="#111"/></svg>
      <span class="candidate-name">Owen Bradley Carter</span>
      <span class="candidate-votes">295</span>
    </div>
    <div class="vote-bar"><div class="vote-bar-fill"></div></div>
  </section>

  <section class="candidate col-left row-3">
    <div class="candidate-photo" role="img" aria-label="Candidate photo"></div>
    <div class="candidate-banner">
      <svg width="440" height="70" viewBox="0 0 440 70"><polygon points="0,0 322,0 284,70 0,70" fill="#c8232a"/><polygon points="330,0 438,0 400,70 292,70" fill="#111"/></svg>
      <span class="candidate-name">Owen Bradley Carter</span>
      <span class="candidate-votes">295</span>
    </div>
    <div class="vote-bar"><div class="vote-bar-fill"></div></div>
  </section>

  <section class="candidate col-left row-4">
    <div class="candidate-photo" role="img" aria-label="Candidate photo"></div>
    <div class="candidate-banner">
      <svg width="440" height="70" viewBox="0 0 440 70"><polygon points="0,0 322,0 284,70 0,70" fill="#c8232a"/><polygon points="330,0 438,0 400,70 292,70" fill="#111"/></svg>
      <span class="candidate-name">Owen Bradley Carter</span>
      <span class="candidate-votes">295</span>
    </div>
    <div class="vote-bar"><div class="vote-bar-fill"></div></div>
  </section>

  <section class="candidate col-right row-1">
    <div class="candidate-photo" role="img" aria-label="Candidate photo"></div>
    <div class="candidate-banner">
      <svg width="440" height="70" viewBox="0 0 440 70"><polygon points="0,0 322,0 284,70 0,70" fill="#c8232a"/><polygon points="330,0 438,0 400,70 292,70" fill="#111"/></svg>
      <span class="candidate-name">Owen Bradley Carter</span>
      <span class="candidate-votes">295</span>
    </div>
    <div class="vote-bar"><div class="vote-bar-fill"></div></div>
  </section>

  <section class="candidate col-right row-2">
    <div class="candidate-photo" role="img" aria-label="Candidate photo"></div>
    <div class="candidate-banner">
      <svg width="440" height="70" viewBox="0 0 440 70"><polygon points="0,0 322,0 284,70 0,70" fill="#c8232a"/><polygon points="330,0 438,0 400,70 292,70" fill="#111"/></svg>
      <span class="candidate-name">Owen Bradley Carter</span>
      <span class="candidate-votes">295</span>
    </div>
    <div class="vote-bar"><div class="vote-bar-fill"></div></div>
  </section>

  <section class="candidate col-right row-3">
    <div class="candidate-photo" role="img" aria-label="Candidate photo"></div>
    <div class="candidate-banner">
      <svg width="440" height="70" viewBox="0 0 440 70"><polygon points="0,0 322,0 284,70 0,70" fill="#c8232a"/><polygon points="330,0 438,0 400,70 292,70" fill="#111"/></svg>
      <span class="candidate-name">Owen Bradley Carter</span>
      <span class="candidate-votes">295</span>
    </div>
    <div class="vote-bar"><div class="vote-bar-fill"></div></div>
  </section>

  <section class="candidate col-right row-4">
    <div class="candidate-photo" role="img" aria-label="Candidate photo"></div>
    <div class="candidate-banner">
      <svg width="440" height="70" viewBox="0 0 440 70"><polygon points="0,0 322,0 284,70 0,70" fill="#c8232a"/><polygon points="330,0 438,0 400,70 292,70" fill="#111"/></svg>
      <span class="candidate-name">Owen Bradley Carter</span>
      <span class="candidate-votes">295</span>
    </div>
    <div class="vote-bar"><div class="vote-bar-fill"></div></div>
  </section>

  <div class="footer-band"></div>
</main>
</body>
</html>
```